Security Warning Sign

We have an existing sign that needs an update. I have attached a picture of the current square sign. We need to maintain the same wording. It needs to be professional and appropriate to attach to our customers fence. Also attached is a copy of our building sign which may lend some inspiration and hopefully the ai format will assist. The final sign will be 600mm x 600mmOur website is www.halvorngate.com.au

```html
<!DOCTYPE html>
<html lang="en">
<head>
<meta charset="utf-8">
<title>Security Warning Signs</title>
<link rel="stylesheet" href="https://fonts.googleapis.com/css2?family=Anton&family=Arimo:wght@700&family=Open+Sans:wght@700;800&display=swap">
<style>
  :root {
    --backdrop: #675856;
    --sign-red: #d0080a;
    --sign-black: #0c0c0c;
    --ink-white: #ffffff;
    --accent-orange: #f7801e;
    --camera-dark: #2a2a2a;
    --camera-mid: #4a4a4a;
  }
  * { margin: 0; padding: 0; box-sizing: border-box; }
  html, body {
    width: 1200px; height: 1200px; overflow: hidden;
    background: var(--backdrop);
  }
  .canvas { position: relative; width: 1200px; height: 1200px; }

  .sign { position: absolute; left: 0; width: 1200px; height: 600px; }
  .sign--upper { top: 0; }
  .sign--lower { top: 568px; }

  .sign__frame, .sign__panel { position: absolute; }
  .sign--upper .sign__frame {
    left: 326px; top: 48px; width: 544px; height: 542px;
    border-radius: 50px; background: var(--sign-black);
  }
  .sign--upper .sign__panel {
    left: 343px; top: 62px; width: 510px; height: 512px;
    border-radius: 38px; background: var(--sign-red);
  }
  .sign--lower .sign__frame {
    left: 318px; top: 48px; width: 558px; height: 554px;
    border-radius: 50px; background: var(--sign-red);
  }
  .sign--lower .sign__panel {
    left: 335px; top: 64px; width: 524px; height: 522px;
    border-radius: 38px; background: var(--sign-black);
  }

  .sign__headline {
    position: absolute; left: 343px; top: 66px; width: 510px;
    text-align: center;
    font-family: "Anton", Impact, sans-serif;
    font-size: 110px; line-height: 1; letter-spacing: 1px;
  }
  .sign--upper .sign__headline { color: var(--sign-black); }
  .sign--lower .sign__headline { color: var(--sign-red); }

  .sign__line {
    position: absolute; white-space: nowrap;
    font-family: "Arimo", Arial, sans-serif; font-weight: 700;
    color: var(--ink-white); line-height: 1;
  }
  .sign__line--1 { left: 365px; top: 202px; font-size: 37px; }
  .sign__line--2 { left: 365px; top: 252px; font-size: 37px; }
  .sign__line--3 { left: 360px; top: 302px; font-size: 37px; }
  .sign__line--4 { left: 357px; top: 356px; font-size: 37px; }
  .sign__line--big { left: 356px; top: 392px; font-size: 72px; }

  .sign__camera {
    position: absolute; left: 694px; top: 196px; width: 158px; height: 92px;
    border-radius: 26px 14px 14px 40px;
    background: linear-gradient(160deg, var(--camera-mid), var(--camera-dark));
  }

  .brand {
    position: absolute; left: 512px; top: 468px;
    display: flex; align-items: center; gap: 10px;
  }
  .brand__dot {
    width: 62px; height: 62px; border-radius: 50%;
    background: var(--accent-orange);
  }
  .brand__name {
    font-family: "Open Sans", Arial, sans-serif; font-weight: 800;
    font-size: 18px; line-height: 23px; color: var(--ink-white);
    text-transform: uppercase;
  }

  .sign__web {
    position: absolute; left: 451px; top: 551px;
    font-family: "Open Sans", Arial, sans-serif; font-weight: 700;
    font-size: 12.5px; color: var(--ink-white); text-transform: uppercase;
  }
  .sign__phone {
    position: absolute; left: 684px; top: 542px; width: 169px; height: 32px;
    display: flex; align-items: center; justify-content: flex-end; gap: 7px;
    padding-right: 14px;
    background: var(--accent-orange);
    clip-path: polygon(14px 0, 100% 0, 100% 100%, 0 100%);
    font-family: "Open Sans", Arial, sans-serif; font-weight: 700;
    font-size: 16px; color: var(--ink-white);
  }
  .sign--upper .sign__phone { border-bottom-right-radius: 30px; }
  .sign__phone svg { width: 16px; height: 16px; }
</style>
</head>
<body>
<main class="canvas">

  <section class="sign sign--upper">
    <div class="sign__frame"></div>
    <div class="sign__panel"></div>
    <h1 class="sign__headline">WARNING</h1>
    <p class="sign__line sign__line--1">ELECTRONIC</p>
    <p class="sign__line sign__line--2">SURVEILLANCE</p>
    <p class="sign__line sign__line--3">AND RECORDING</p>
    <p class="sign__line sign__line--4">DEVICES INSTALLED</p>
    <p class="sign__line sign__line--big">IN THIS AREA</p>
    <div class="sign__camera" role="img" aria-label="Illustration of a wall-mounted security camera"></div>
    <div class="brand">
      <span class="brand__dot"></span>
      <span class="brand__name">Halvorngate<br>Security<br>Services</span>
    </div>
    <p class="sign__web">www.halvorngate.com.au</p>
    <p class="sign__phone">
      <svg viewBox="0 0 24 24" aria-hidden="true"><path fill="#fff" d="M6.6 10.8a15.1 15.1 0 0 0 6.6 6.6l2.2-2.2a1 1 0 0 1 1-.25 11.4 11.4 0 0 0 3.6.57 1 1 0 0 1 1 1V20a1 1 0 0 1-1 1A17 17 0 0 1 3 4a1 1 0 0 1 1-1h3.5a1 1 0 0 1 1 1c0 1.25.2 2.45.57 3.57a1 1 0 0 1-.25 1z"/></svg>
      1300 555 018
    </p>
  </section>

  <section class="sign sign--lower">
    <div class="sign__frame"></div>
    <div class="sign__panel"></div>
    <h2 class="sign__headline">WARNING</h2>
    <p class="sign__line sign__line--1">ELECTRONIC</p>
    <p class="sign__line sign__line--2">SURVEILLANCE</p>
    <p class="sign__line sign__line--3">AND RECORDING</p>
    <p class="sign__line sign__line--4">DEVICES INSTALLED</p>
    <p class="sign__line sign__line--big">IN THIS AREA</p>
    <div class="sign__camera" role="img" aria-label="Illustration of a wall-mounted security camera"></div>
    <div class="brand">
      <span class="brand__dot"></span>
      <span class="brand__name">Halvorngate<br>Security<br>Services</span>
    </div>
    <p class="sign__web">www.halvorngate.com.au</p>
    <p class="sign__phone">
      <svg viewBox="0 0 24 24" aria-hidden="true"><path fill="#fff" d="M6.6 10.8a15.1 15.1 0 0 0 6.6 6.6l2.2-2.2a1 1 0 0 1 1-.25 11.4 11.4 0 0 0 3.6.57 1 1 0 0 1 1 1V20a1 1 0 0 1-1 1A17 17 0 0 1 3 4a1 1 0 0 1 1-1h3.5a1 1 0 0 1 1 1c0 1.25.2 2.45.57 3.57a1 1 0 0 1-.25 1z"/></svg>
      1300 555 018
    </p>
  </section>

</main>
</body>
</html>
```